Project Managers Business card design

We need business cards for our Project Managers based in Sydney for our business name Korbet Pty Ltd. We project manage property improvements and infrastructure Assets. We provide asset owners Project Management services from original concept, management of architectural and engineering designs, call and select construction tenders, and manage the Asset operational life cycle to conclusion and removal. We are experienced in feasibility studies, risk assessments, quality control, safety control, environmental analysis. We are specialist in Aged Care and Child Care Services. We can provide asset reviewing checklists, asset inspections, contract cost and contract assessments, dispute resolution services and articles and books on safely working and living in environments subject to analysis. the design colours should be queensland marone and NSW sky blue.

Industry/Entity Type

Construction

Contact Information for Business Card

Gavin Trelowe (Mb 0412 847 391), Dennis Marquay (Mb 0438 216 074), Luke Benhadda,(Mb 0421 963 158)
E: all business cards: korbet@fernmail.example
Office phone number (02) 9482 3165
Address
Level 1 Halyard House
47 Wexford Lane, Parramatta
Web: projectmanagers@worksleadsbykorbet.example (to be checked on Printlyne web draft)

```html
<!DOCTYPE html>
<html lang="en">
<head>
<meta charset="utf-8">
<title>Korbet Pty Ltd – Business Card</title>
<link rel="stylesheet" href="https://fonts.googleapis.com/css2?family=Bodoni+Moda:ital,wght@0,400;1,400&display=swap">
<style>
  :root {
    --backdrop-light: #dde2ee;
    --backdrop-mid: #c4c6ce;
    --backdrop-dark: #a9a8ad;
    --navy-blue: #2c4ca6;
    --navy-blue-deep: #22409a;
    --sky-blue: #7f9ce6;
    --sky-blue-soft: #98b0e6;
    --sky-blue-dusk: #6a80c0;
    --maroon: #7a1f3a;
    --maroon-soft: #8c6a72;
    --badge-shadow: #2a2a33;
    --ink: #111114;
    --font-serif: "Bodoni Moda", "Didot", serif;
  }
  html, body {
    margin: 0;
    padding: 0;
    width: 1200px;
    height: 685px;
    overflow: hidden;
  }
  .canvas {
    position: relative;
    width: 1200px;
    height: 685px;
    overflow: hidden;
    background:
      radial-gradient(ellipse 420px 200px at 560px 10px, var(--backdrop-light), transparent 70%),
      radial-gradient(ellipse 700px 500px at 600px 340px, var(--backdrop-mid), var(--backdrop-dark));
    font-family: var(--font-serif);
    color: var(--ink);
  }
  .card-art {
    position: absolute;
    left: 0;
    top: 0;
  }
  .company-name {
    position: absolute;
    left: 135px;
    top: 100px;
    margin: 0;
    font-size: 92px;
    font-weight: 400;
    line-height: 1;
    letter-spacing: -1px;
    white-space: nowrap;
  }
  .manager-name {
    position: absolute;
    left: 133px;
    top: 318px;
    margin: 0;
    font-size: 34px;
    font-style: italic;
    font-weight: 400;
    white-space: nowrap;
  }
  .contact-list {
    position: absolute;
    left: 150px;
    top: 398px;
    margin: 0;
    padding: 0;
    list-style: none;
    white-space: nowrap;
  }
  .contact-list .email {
    font-size: 32px;
    line-height: 46px;
  }
  .contact-list .office-phone,
  .contact-list .address,
  .contact-list .website {
    font-size: 30px;
    line-height: 44px;
  }
  .contact-list .address,
  .contact-list .website {
    margin-left: -3px;
  }
  .contact-list .website {
    color: var(--maroon);
  }
</style>
</head>
<body>
<main class="canvas">
  <svg class="card-art" width="1200" height="685" viewBox="0 0 1200 685" aria-hidden="true">
    <defs>
      <radialGradient id="sky-panel" cx="0.62" cy="0.35" r="0.7">
        <stop offset="0" stop-color="var(--sky-blue)"/>
        <stop offset="0.55" stop-color="var(--sky-blue-soft)"/>
        <stop offset="1" stop-color="var(--sky-blue-dusk)"/>
      </radialGradient>
      <radialGradient id="navy-panel" cx="0.35" cy="0.65" r="0.8">
        <stop offset="0" stop-color="var(--navy-blue)"/>
        <stop offset="1" stop-color="var(--navy-blue-deep)"/>
      </radialGradient>
    </defs>
    <rect class="card-panel-sky" x="49" y="41" width="1099" height="610" fill="url(#sky-panel)"/>
    <polygon class="card-panel-navy" points="49,41 1148,651 49,651" fill="url(#navy-panel)"/>
    <ellipse class="badge-shadow" cx="160" cy="164" rx="115" ry="103" fill="var(--badge-shadow)"/>
    <ellipse class="badge" cx="165" cy="169" rx="112" ry="100" fill="var(--maroon-soft)"/>
  </svg>

  <h1 class="company-name">Korbet Pty Ltd</h1>
  <p class="manager-name">*Dennis Marquay (Mb 0438 216 074)</p>
  <ul class="contact-list">
    <li class="email">korbet@fernmail.example</li>
    <li class="office-phone">Office phone number (02) 9482 3165</li>
    <li class="address">Level 1 Halyard House 47 Wexford Lane, Parramatta</li>
    <li class="website">projectmanagers@worksleadsbykorbet.example</li>
  </ul>
</main>
</body>
</html>
```